Business Card Design - Photographer

I am a landscape photographer and I require a business card design. 

I require two designs:
1)  a double sided business card
 and
b)  a single sided business card 

The single sided design can either be the same as the double sided (with just one side having all the information)....or it can be an entire new design. Its up to you.

My corporate colours are (CMYK):

Blue   69, 32, 0, 0
Grey  72,  64,  47,  31
Green  32,  2,  91,  0
Yellow   0, 19, 92, 0
Orange  0, 39, 75, 0

Colour space in final file should be in CMYK.

The details that need to be included on the card:

- Use the provided Logo
- Name: Lukas Wendrovski
- Email:   sales@vistaplume.com.au
- Website:    vistaplume.com.au
- Twitter:    twitter.com/vistaplume
- Facebook:   facebook.com/vistaplume
- Mobile  0415 309 662

Please use the attached template to design the logo to the specified size, including the marked bleed lines. I have also attached my logo in PNG (transparent background) and ai format for you to use.

The final file should be:
- Photoshop version with layers so I can edit the name/text etc. All non vector files should be high resolution at 1039 x 697 pixels at 300 dpi.

I also require a file as:
- Vector based PDF

Anyway questions please contact me.

Thank you

Industry/Entity Type

Landscape

Logo styles of interest
Pictorial/Combination Logo
Abstract Logo
Wordmark Logo
Lettermark Logo
Requirements
Must have
• The details that need to be included on the card:

- Use the provided Logo
- Name: Lukas Wendrovski
- Email: sales@vistaplume.com.au
- Website: vistaplume.com.au
- Twitter: twitter.com/vistaplume
- Facebook: facebook.com/vistaplume
- Mobile 0415 309 662

```html
<!DOCTYPE html>
<html lang="en">
<head>
<meta charset="utf-8">
<title>Vista Plume – Business Card</title>
<link rel="stylesheet" href="https://fonts.googleapis.com/css2?family=Cinzel:wght@500&display=swap">
<style>
  :root {
    --card-yellow: #fecb1a;
    --brand-navy: #283257;
    --sky-dark: #3a4350;
    --sky-mid: #6c6a5a;
    --sun-gold: #e9b93a;
    --haze-amber: #b7933e;
    --hill-olive: #6f6a2c;
    --scrub-green: #4f6a2a;
  }
  html, body {
    margin: 0;
    padding: 0;
    width: 1200px;
    height: 806px;
    overflow: hidden;
    background: var(--card-yellow);
  }
  .card {
    position: relative;
    width: 1200px;
    height: 806px;
    background: var(--card-yellow);
    overflow: hidden;
  }
  .card-art {
    position: absolute;
    inset: 0;
  }
  .brand {
    position: absolute;
    left: 55px;
    top: 129px;
    width: 296px;
    text-align: center;
  }
  .brand-dot {
    display: block;
    width: 110px;
    height: 110px;
    margin: 0 auto 14px;
    border-radius: 50%;
    background: var(--brand-navy);
  }
  .brand-name {
    margin: 0;
    font-family: "Cinzel", serif;
    font-weight: 500;
    font-size: 32px;
    letter-spacing: 0.5px;
    color: var(--brand-navy);
    white-space: nowrap;
  }
</style>
</head>
<body>
  <main class="card">
    <svg class="card-art" width="1200" height="806" viewBox="0 0 1200 806">
      <defs>
        <linearGradient id="landscape-tone" x1="0" y1="0" x2="0" y2="1">
          <stop offset="0" stop-color="var(--sky-dark)"/>
          <stop offset="0.3" stop-color="var(--sky-mid)"/>
          <stop offset="0.45" stop-color="var(--sun-gold)"/>
          <stop offset="0.6" stop-color="var(--haze-amber)"/>
          <stop offset="0.75" stop-color="var(--hill-olive)"/>
          <stop offset="1" stop-color="var(--scrub-green)"/>
        </linearGradient>
      </defs>
      <path class="landscape-panel" role="img"
            aria-label="Landscape photograph: mountain ridge at sunset under dark clouds, green scrub in the foreground"
            fill="url(#landscape-tone)"
            d="M885 0 H1200 V806 H885 A10 10 0 0 1 875 796 V181 H843 A10 10 0 0 1 833 171 V60 A10 10 0 0 1 843 50 H875 V10 A10 10 0 0 1 885 0 Z"/>
      <circle class="accent-ring" cx="1142" cy="420" r="162" fill="none"
              stroke="var(--card-yellow)" stroke-width="56"/>
    </svg>

    <div class="brand">
      <span class="brand-dot"></span>
      <p class="brand-name">VISTA PLUME</p>
    </div>
  </main>
</body>
</html>
```